The Verdant Ledger App - Modernization & Graphics User Interface Friendliness Updates

We are Verdant Ledger, and we want to bring a new branding look and graphical user interface to the Verdant Ledger App. The app is a quick reference encyclopedia for all things produce. Boasting articles on over 2,000 produce items, with information ranging from taste and application to geographical and cultural significance. Included in its features are over 10 thousand recipes, and the Verdant Ledger App Harvest Circle – a global initiative to connect farmer, customer, and chef in one sustainable and easy to use application. The design needs to bring a greater sense of social connection – encouraging the user to participate in the 'Harvest Circled' experience voluntarily. The design should reflect a sense of authority reflecting the authenticity and reliability of the provided information, it's writing, and its sources. Download the App here: vledgr.example/install

Target Market(s)

Women and Men between ages 21-55.

Industry/Entity Type

Education

Font styles to use
Serif
Sans Serif

Colors

Designer to choose colors to be used in the design.

Requirements
Must have
• An updated user interface, the intuitive usability of the app is currently non-existent. We are looking to reflect as the authority on produce. The app design must reflect a professional, user-friendly, up-to-date, and trustworthy feel.
Nice to have
• To incorporate the social draw of the Harvest Circle we would like to include on the home page "Social Bubbles" (think Pictoloop stories) which updates with shared photos of produce and their location.
Should not have
• An overly complicated theme, distracting or unprofessional colors, and images.

```html
<!DOCTYPE html>
<html lang="en">
<head>
<meta charset="utf-8">
<title>Verdant Ledger App – Screen Flow</title>
<link href="https://fonts.googleapis.com/css2?family=Open+Sans:wght@300;400;600;700&family=Parisienne&display=swap" rel="stylesheet">
<style>
  :root{
    --board-green:#00a04c;
    --label-ink:#2b2b2b;
    --app-green:#1f9a45;
    --app-green-dark:#137a34;
    --wood-light:#8f7f6b;
    --wood-mid:#6b5c4b;
    --wood-dark:#3e342a;
    --sign-orange:#f7a531;
    --nav-gold:#8b6a1c;
    --badge-red:#e0262b;
    --tile-white:#ffffff;
    --fruit-text:#1d7a2f;
  }
  *{box-sizing:border-box;margin:0;padding:0}
  html,body{width:1200px;height:560px;overflow:hidden;background:var(--board-green)}
  body{font-family:"Open Sans",Arial,sans-serif;position:relative}
  .board{position:relative;width:1200px;height:560px}

  .screen-title{position:absolute;top:42px;font-size:16px;color:var(--label-ink);transform:translateX(-50%);white-space:nowrap}
  .screen-title.bold{font-weight:700}
  .screen-title.light{font-weight:300}

  .note{position:absolute;color:var(--label-ink);font-size:10.5px;text-align:center;line-height:1.25;transform:translateX(-50%);white-space:nowrap}
  .note.big{font-size:15.5px;font-weight:700;line-height:1.25}
  .arrows{position:absolute;left:0;top:0;pointer-events:none}

  .screen{position:absolute;top:118px;width:182px;height:323px;overflow:hidden;box-shadow:4px 5px 8px rgba(0,0,0,.45);background:var(--wood-dark)}
  .backdrop{position:absolute;inset:0}
  .wood{background:linear-gradient(175deg,var(--wood-light) 0%,#7d6e5c 30%,var(--wood-mid) 60%,var(--wood-dark) 100%)}
  .produce-scene{position:absolute;left:0;right:0;bottom:0;height:56%;
    background:linear-gradient(180deg,rgba(62,52,42,0) 0%,rgba(120,40,24,.75) 22%,#9c2a1a 40%,#c98a2a 58%,#d9b650 72%,#a8461c 86%,#5e1d12 100%)}
  .blur-scene{background:linear-gradient(180deg,#4e4030 0%,#6b5238 18%,#9c7a3c 40%,#c9a35a 55%,#a0603a 75%,#6a3a26 100%)}

  .brand{position:absolute;left:0;right:0;text-align:center;color:#2a2a2a}
  .brand-name{display:inline-flex;align-items:center;gap:6px;font-size:17px;font-weight:700;letter-spacing:.3px}
  .brand-name .dot{width:10px;height:10px;border-radius:50%;background:#2a2a2a;display:inline-block}
  .brand-url{font-size:5.5px;letter-spacing:.6px;margin-top:3px}
  .tagline{position:absolute;top:104px;left:0;right:0;text-align:center;font-family:"Parisienne",cursive;color:#fff;font-size:16px;line-height:1.3;text-shadow:0 1px 2px rgba(0,0,0,.4)}

  .field{position:absolute;left:20px;right:20px;height:18px;border-bottom:1px solid rgba(255,255,255,.75);color:#fff;font-size:6px;display:flex;align-items:center;padding-left:14px}
  .field svg{position:absolute;left:0;top:3px}
  .sign-in{position:absolute;left:13px;width:158px;top:265px;height:26px;border-radius:13px;background:var(--sign-orange);color:#2a2a2a;font-size:12px;display:flex;align-items:center;justify-content:center}
  .signup-hint{position:absolute;top:306px;left:0;right:0;text-align:center;color:#fff;font-size:5.5px}

  .app-bar{position:absolute;top:0;left:0;right:0;height:34px;display:flex;align-items:center;justify-content:center;color:#fff;font-size:7px;font-weight:600}
  .app-bar .left{position:absolute;left:7px;top:11px}
  .app-bar .right{position:absolute;right:7px;top:10px}

  .search{position:absolute;top:37px;left:4px;right:4px;height:17px;border-radius:9px;background:#fff;color:var(--app-green);font-size:7px;display:flex;align-items:center;justify-content:center}
  .search svg{position:absolute;right:7px;top:4px}
  .menu-band{position:absolute;top:58px;left:0;right:0;height:18px;background:var(--app-green);color:#fff;font-size:11px;font-weight:600;display:flex;align-items:center;justify-content:center}
  .menu-band svg{position:absolute;right:8px;top:6px}

  .tile-grid{position:absolute;top:79px;left:0;right:0;display:grid;grid-template-columns:1fr 1fr;gap:3px;padding:0 1px;background:#d9d9d9}
  .tile{background:var(--tile-white);height:84px;display:flex;flex-direction:column;align-items:center;justify-content:flex-end;padding-bottom:6px;font-size:7.5px;color:#333;text-align:center;line-height:1.15}
  .tile .art{width:84px;height:52px;margin-bottom:4px}
  .tile.short{height:46px;justify-content:flex-start;padding-top:6px}

  .title-band{position:absolute;top:34px;left:20px;right:20px;height:24px;background:var(--app-green);color:#fff;font-size:8px;font-weight:600;display:flex;align-items:center;justify-content:center}

  .fruit-grid{position:absolute;top:66px;left:10px;right:10px;display:grid;grid-template-columns:76px 76px;justify-content:space-between;row-gap:8px}
  .fruit{height:37px;background:rgba(255,255,255,.6);box-shadow:0 1px 3px rgba(0,0,0,.25);display:flex;align-items:center;justify-content:center;text-align:center;color:var(--fruit-text);font-size:7.5px;font-weight:600;line-height:1.2;padding:0 3px}

  .product-photo{position:absolute;top:58px;left:0;right:0;height:89px;background:#fff}
  .product-photo .art{position:absolute;inset:4px 6px}
  .tab-rows{position:absolute;top:147px;left:0;right:0;height:48px;background:rgba(255,255,255,.88)}
  .tabs{position:absolute;left:6px;right:6px;display:flex;justify-content:space-between;font-size:5.5px;color:#333}
  .tabs .active{font-weight:700;border-bottom:1px solid #333}
  .tabs.row1{top:5px}
  .tabs.row2{top:24px;padding:0 2px}
  .tab-rows .rule{position:absolute;left:0;right:0;height:1px;background:#6d5a3a}
  .description{position:absolute;top:199px;left:4px;right:4px;height:90px;background:rgba(255,255,255,.55);color:var(--fruit-text);font-size:5.6px;font-weight:700;text-align:center;line-height:1.38;padding:3px 4px}

  .nav{position:absolute;left:0;right:0;bottom:0;height:29px;background:#fff;display:flex;justify-content:space-around;align-items:center}
  .nav.ghost{background:rgba(255,255,255,.82)}
  .nav .bubble{position:relative}
  .nav .badge{position:absolute;top:-5px;right:-5px;width:8px;height:8px;border-radius:50%;background:var(--badge-red);color:#fff;font-size:5px;display:flex;align-items:center;justify-content:center}
  .nav-under{position:absolute;bottom:1px;left:0;right:0;display:flex;justify-content:space-around;font-size:7px;color:rgba(0,0,0,.2);z-index:2;pointer-events:none}
</style>
</head>
<body>
<div class="board">

  <div class="screen-title bold" style="left:145px">Splash Screen</div>
  <div class="screen-title light" style="left:376px">Login Screen</div>
  <div class="screen-title bold" style="left:608px">Categories Screen</div>
  <div class="screen-title light" style="left:828px">all Fruits Screen</div>
  <div class="screen-title bold" style="left:1057px">Detailed Product View</div>

  <div class="note" style="left:483px;top:80px">Dropdown Menu to select<br>Produce or Receipe</div>
  <div class="note" style="left:661px;top:64px">Profile<br>Settings</div>
  <div class="note" style="left:406px;top:490px">Sign up screen will come after thistt</div>
  <div class="note" style="left:706px;top:487px">Sharing</div>
  <div class="note big" style="left:606px;top:497px">Social Bubble for<br>Stories . After Clicking this<br>on next screen one can add stores and share</div>

  <!-- Splash -->
  <section class="screen" style="left:54px">
    <div class="backdrop wood" role="img" aria-label="Weathered wooden board backdrop"></div>
    <div class="produce-scene" role="img" aria-label="Photo of corn, apples, peppers, grapes and a wooden spoon on a table"></div>
    <div class="brand" style="top:34px">
      <div class="brand-name"><span class="dot"></span>Verdant Ledger</div>
      <div class="brand-url">www.verdantledger.example</div>
    </div>
    <div class="tagline">Sharing the story of<br>fruits and vegetables</div>
  </section>

  <!-- Login -->
  <section class="screen" style="left:286px">
    <div class="backdrop wood" role="img" aria-label="Weathered wooden board backdrop"></div>
    <div class="produce-scene" style="height:62%;opacity:.85" role="img" aria-label="Photo of corn, apples, grapes and a wooden spoon, dimmed behind the form"></div>
    <div class="brand" style="top:80px">
      <div class="brand-name"><span class="dot"></span>Verdant Ledger</div>
      <div class="brand-url">www.verdantledger.example</div>
    </div>
    <div class="field" style="top:196px">
      <svg width="9" height="9" viewBox="0 0 10 10"><circle cx="5" cy="3" r="2.2" fill="none" stroke="#fff"/><path d="M1 10c0-3 8-3 8 0" fill="none" stroke="#fff"/></svg>Username
    </div>
    <div class="field" style="top:226px">
      <svg width="9" height="9" viewBox="0 0 10 10"><rect x="1.5" y="4.5" width="7" height="5" fill="none" stroke="#fff"/><path d="M3 4.5V3a2 2 0 0 1 4 0v1.5" fill="none" stroke="#fff"/></svg>Password
    </div>
    <div class="sign-in">Sign in</div>
    <div class="signup-hint">Don't have an account?&nbsp; Sign Up</div>
  </section>

  <!-- Categories -->
  <section class="screen" style="left:517px;background:#fff">
    <div class="app-bar wood">
      <svg class="left" width="12" height="10" viewBox="0 0 12 10"><path d="M0 1h12M0 5h12M0 9h12" stroke="#fff" stroke-width="1.4"/></svg>
      CATEGORIES
      <svg class="right" width="11" height="11" viewBox="0 0 10 10"><circle cx="5" cy="3" r="2.2" fill="none" stroke="#fff"/><path d="M1 10c0-3 8-3 8 0" fill="none" stroke="#fff"/></svg>
    </div>
    <div style="position:absolute;top:34px;left:0;right:0;height:45px;background:var(--app-green)"></div>
    <div class="search">Search
      <svg width="9" height="9" viewBox="0 0 10 10"><circle cx="4" cy="4" r="3" fill="none" stroke="#333"/><path d="M6.3 6.3L9 9" stroke="#333"/></svg>
    </div>
    <div class="menu-band">Produce
      <svg width="9" height="6" viewBox="0 0 9 6"><path d="M1 1l3.5 3.5L8 1" fill="none" stroke="#fff" stroke-width="1.3"/></svg>
    </div>
    <div class="tile-grid">
      <div class="tile"><div class="art" role="img" aria-label="Photo of a heap of mixed fruit" style="background:radial-gradient(ellipse 50% 48% at 50% 55%,#d8341c 0%,#e88a1e 45%,#f3c04a 70%,rgba(255,255,255,0) 100%)"></div>All Fruits</div>
      <div class="tile"><div class="art" role="img" aria-label="Photo of a heap of mixed vegetables" style="background:radial-gradient(ellipse 50% 48% at 50% 55%,#d0401c 0%,#6aa02c 45%,#9cc34a 70%,rgba(255,255,255,0) 100%)"></div>All Vegetables</div>
      <div class="tile"><div class="art" role="img" aria-label="Photo of Japanese specialty produce" style="background:radial-gradient(ellipse 50% 40% at 50% 58%,#7a2a2a 0%,#6a5a3a 45%,#8aa04a 70%,rgba(255,255,255,0) 100%)"></div>Japanese<br>Specialities</div>
      <div class="tile"><div class="art" role="img" aria-label="Photo of assorted produce with a spotted-eye mark" style="background:radial-gradient(ellipse 50% 48% at 50% 55%,#c3301a 0%,#3f7a2a 45%,#e0a030 70%,rgba(255,255,255,0) 100%)"></div>Spotted Produce</div>
      <div class="tile short"><div class="art" role="img" aria-label="Photo of Asian specialty produce" style="height:38px;background:radial-gradient(ellipse 50% 60% at 50% 70%,#e0b040 0%,#b0a030 45%,#7a9a3a 70%,rgba(255,255,255,0) 100%)"></div></div>
      <div class="tile short"><div class="art" role="img" aria-label="Photo of seasonal produce" style="height:38px;background:radial-gradient(ellipse 50% 60% at 50% 70%,#e8c840 0%,#8aa63a 45%,#5e8a2c 70%,rgba(255,255,255,0) 100%)"></div></div>
    </div>
    <nav class="nav ghost">
      <svg width="12" height="11" viewBox="0 0 12 11"><path d="M1 5.5L6 1l5 4.5M2.5 4.5V10h7V4.5" fill="none" stroke="#8b6a1c"/></svg>
      <svg width="14" height="9" viewBox="0 0 14 9"><path d="M1 4.5C4 0 10 0 13 4.5 10 9 4 9 1 4.5z" fill="none" stroke="#8b6a1c"/><circle cx="7" cy="4.5" r="2" fill="#8b6a1c"/></svg>
      <span class="bubble"><svg width="12" height="11" viewBox="0 0 12 11"><path d="M1 1h10v7H5l-3 2.5V8H1z" fill="#8b6a1c"/></svg><span class="badge">4</span></span>
      <svg width="12" height="11" viewBox="0 0 12 11"><path d="M6 10L1.5 5.5a2.6 2.6 0 0 1 4.5-3 2.6 2.6 0 0 1 4.5 3z" fill="none" stroke="#8b6a1c"/></svg>
      <svg width="11" height="11" viewBox="0 0 11 11"><circle cx="9" cy="2" r="1.5" fill="none" stroke="#8b6a1c"/><circle cx="2" cy="5.5" r="1.5" fill="none" stroke="#8b6a1c"/><circle cx="9" cy="9" r="1.5" fill="none" stroke="#8b6a1c"/><path d="M3.3 4.8l4.4-2.2M3.3 6.2l4.4 2.2" stroke="#8b6a1c"/></svg>
    </nav>
    <div class="nav-under"><span>Asian Specialities</span><span>Seasonal Produce</span></div>
  </section>

  <!-- All fruits -->
  <section class="screen" style="left:738px">
    <div class="backdrop blur-scene" role="img" aria-label="Blurred photo of corn and vegetables on wood"></div>
    <div class="app-bar wood">
      <svg class="left" width="7" height="11" viewBox="0 0 7 11"><path d="M6 1L1.5 5.5 6 10" fill="none" stroke="#fff" stroke-width="1.3"/></svg>
      PRODUCE
      <svg class="right" width="11" height="11" viewBox="0 0 10 10"><circle cx="5" cy="3" r="2.2" fill="none" stroke="#fff"/><path d="M1 10c0-3 8-3 8 0" fill="none" stroke="#fff"/></svg>
    </div>
    <div style="position:absolute;top:34px;left:0;right:0;height:24px;background:var(--app-green-dark)"></div>
    <div class="title-band">ALL FRUITS</div>
    <div class="fruit-grid">
      <div class="fruit">Akebi Fruit</div><div class="fruit">Apple Ambrosia</div>
      <div class="fruit">Apple Anna</div><div class="fruit">Apple Ashmead's Kernel</div>
      <div class="fruit">Apple Autumn Greeting</div><div class="fruit">Apple Autumn Glory</div>
      <div class="fruit">Apple Belle de Boskoop</div><div class="fruit">Apple Ambrosia</div>
      <div class="fruit">Apple Anna</div><div class="fruit">Apple Ashmead's Kernel</div>
    </div>
    <nav class="nav ghost">
      <svg width="12" height="11" viewBox="0 0 12 11"><path d="M1 5.5L6 1l5 4.5M2.5 4.5V10h7V4.5" fill="none" stroke="#8b6a1c"/></svg>
      <svg width="14" height="9" viewBox="0 0 14 9"><path d="M1 4.5C4 0 10 0 13 4.5 10 9 4 9 1 4.5z" fill="none" stroke="#8b6a1c"/><circle cx="7" cy="4.5" r="2" fill="#8b6a1c"/></svg>
      <span class="bubble"><svg width="12" height="11" viewBox="0 0 12 11"><path d="M1 1h10v7H5l-3 2.5V8H1z" fill="#8b6a1c"/></svg><span class="badge">4</span></span>
      <svg width="12" height="11" viewBox="0 0 12 11"><path d="M6 10L1.5 5.5a2.6 2.6 0 0 1 4.5-3 2.6 2.6 0 0 1 4.5 3z" fill="none" stroke="#8b6a1c"/></svg>
      <svg width="11" height="11" viewBox="0 0 11 11"><circle cx="9" cy="2" r="1.5" fill="none" stroke="#8b6a1c"/><circle cx="2" cy="5.5" r="1.5" fill="none" stroke="#8b6a1c"/><circle cx="9" cy="9" r="1.5" fill="none" stroke="#8b6a1c"/><path d="M3.3 4.8l4.4-2.2M3.3 6.2l4.4 2.2" stroke="#8b6a1c"/></svg>
    </nav>
  </section>

  <!-- Detailed product -->
  <section class="screen" style="left:966px">
    <div class="backdrop blur-scene" role="img" aria-label="Blurred photo of corn and vegetables on wood"></div>
    <div class="app-bar wood">
      <svg class="left" width="7" height="11" viewBox="0 0 7 11"><path d="M6 1L1.5 5.5 6 10" fill="none" stroke="#fff" stroke-width="1.3"/></svg>
      PRODUCE &gt; ALL FRUITS
    </div>
    <div style="position:absolute;top:34px;left:0;right:0;height:24px;background:var(--app-green-dark)"></div>
    <div class="title-band">AKEBI FRUIT</div>
    <div class="product-photo"><div class="art" role="img" aria-label="Photo of three purple akebi fruits, one split open" style="background:radial-gradient(ellipse 48% 46% at 50% 50%,#3e3282 0%,#5a4aa2 45%,#8a7ab8 68%,rgba(255,255,255,0) 100%)"></div></div>
    <div class="tab-rows">
      <div class="rule" style="top:0"></div>
      <div class="tabs row1"><span class="active">Description &amp; Taste</span><span>|</span><span>Availability</span><span>|</span><span>Interesting Facts</span></div>
      <div class="rule" style="top:16px"></div>
      <div class="tabs row2"><span>Applications</span><span>Geography and History</span><span>Recipes</span></div>
      <div class="rule" style="top:40px"></div>
    </div>
    <div class="description">Akebi fruit has a purple color not often seen in nature. It is the size of a Russet potato and is soft to the touch. A slice can be removed from the thick rind of a domesticated Akebi fruit, whereas the wild grown fruits must be allowed to split on their own indicating ripeness and is soft to the touch. A slice can be removed from the thick rind of a domesticated Akebi fruit, whereas the wild grown fruits must be allowed to split on their own . indicating ripeness</div>
    <nav class="nav">
      <svg width="12" height="11" viewBox="0 0 12 11"><path d="M1 5.5L6 1l5 4.5M2.5 4.5V10h7V4.5" fill="none" stroke="#8b6a1c"/></svg>
      <svg width="14" height="9" viewBox="0 0 14 9"><path d="M1 4.5C4 0 10 0 13 4.5 10 9 4 9 1 4.5z" fill="none" stroke="#8b6a1c"/><circle cx="7" cy="4.5" r="2" fill="#8b6a1c"/></svg>
      <span class="bubble"><svg width="12" height="11" viewBox="0 0 12 11"><path d="M1 1h10v7H5l-3 2.5V8H1z" fill="#8b6a1c"/></svg><span class="badge">4</span></span>
      <svg width="12" height="11" viewBox="0 0 12 11"><path d="M6 10L1.5 5.5a2.6 2.6 0 0 1 4.5-3 2.6 2.6 0 0 1 4.5 3z" fill="none" stroke="#8b6a1c"/></svg>
      <svg width="11" height="11" viewBox="0 0 11 11"><circle cx="9" cy="2" r="1.5" fill="none" stroke="#8b6a1c"/><circle cx="2" cy="5.5" r="1.5" fill="none" stroke="#8b6a1c"/><circle cx="9" cy="9" r="1.5" fill="none" stroke="#8b6a1c"/><path d="M3.3 4.8l4.4-2.2M3.3 6.2l4.4 2.2" stroke="#8b6a1c"/></svg>
    </nav>
  </section>

  <svg class="arrows" width="1200" height="560" viewBox="0 0 1200 560">
    <defs>
      <marker id="arrowhead" viewBox="0 0 10 10" refX="8" refY="5" markerWidth="6" markerHeight="6" orient="auto-start-reverse">
        <path d="M0 0L10 5 0 10z" fill="#111"/>
      </marker>
    </defs>
    <g stroke="#111" stroke-width="2" fill="none">
      <line x1="485" y1="113" x2="530" y2="188" marker-end="url(#arrowhead)"/>
      <line x1="678" y1="134" x2="657" y2="98" marker-end="url(#arrowhead)"/>
      <line x1="398" y1="484" x2="398" y2="438" marker-end="url(#arrowhead)"/>
      <line x1="608" y1="487" x2="608" y2="440" marker-end="url(#arrowhead)"/>
      <line x1="710" y1="478" x2="686" y2="442" marker-end="url(#arrowhead)"/>
    </g>
  </svg>
</div>
</body>
</html>
```